Website design for Cambridge based systematic hedge fund

We have run previous craftmosaic competitions to design our company logo, business cards and the styling of our presentation deck (see attached files).
As the final step we are looking to get a website designed that is thematically consistent with these existing elements of our branding.
You can find some of our competitors websites below:
https://www.quelmarsh.example/
https://www.fenloor.example/
https://www.pyvart.example/
https://www.dulvet.example/
https://www.orbelmfunds.example/
https://www.valtrigo.example/
https://www.meskilfunds.example/home
We would like to have a website that works well on both mobile devices and desktops. Either just as one page that can be scrolled down, with links at the top that skips to certain sections, or a few separate pages that can be navigated by a top menu.
It should look professional, we are not after lots of animations or unnecessary transitions, and in particular the website must be smooth to navigate. We would like to avoid having peoples of people, we are happy to make use of elements from the presentation (for example the style of the cover slide, or the section slides with the faded bridge in the background), or 'financial' style images.
We would like to have the following sections for now. For some of these some example text has been provided, final text may change but it will be of similar length. For the other sections we are happy to just have template text for now. At the moment we are mainly interested to see styles/layouts as words can be added easily afterwards:
1) We will need a disclaimer pop up the first time someone visits the site (see for example the meskilfunds example).
2) Top page - company name, then in larger text "Bringing AI and Statistical Inference to Financial Markets", and somewhere in smaller text "Harlow Vectors is a quantitative asset manager with the singular focus of delivering algorithmic strategies that work"
3) "About us" section: will describe us as a company, details our approach, company values, and explains the company logo.
Example text:
"We deliver consistent alpha across liquid markets through the application of proprietary IP in Bayesian inference, machine learning and artificial intelligence. We are a multi-disciplinary team founded by experienced finance professionals from premier institutions, leading academics from the Thornbury Stellar Unit at Ashmere College and world-class software engineers.
Our logo portrays a sillhoute of the lattice walkway at Ashmere College. Our unique scientific approach allows us to bridge cutting-edge mathematical research and computing expertise with financial knowledge to bring algorithmns that work to liquid markets"
4) Hiring section, detailing our culture, what we are looking for.
Example text:
"We are always looking for exceptional talent to join our entrepreneurial team. We are looking for individuals who are creative thinkers, can demonstrate analytical rigour and are passionate about the intersection of science, finance and technology.
We prioritise having a company culture that promotes sharing ideas in a safe, collaborative research environment. We make sure that every member of the team has the oppertunity to explore their own ideas through weekly 'innovation time', and ensure that everyone gets the support they need to continue to grow as individuals within the company."
5) A section for news/press releases
6) Contact us area at the bottom with office location and email. We will need to list 3 addresses for our Cambridge, London and Singapore offices, along with a couple of contact emails or phone numbers
7) A client login button at the top that will take them to a different website (unrelated to this one).

```html
<!DOCTYPE html>
<html lang="en">
<head>
<meta charset="utf-8">
<title>Harlow Vectors — Bringing AI and Statistical Inference to Financial Markets</title>
<link href="https://fonts.googleapis.com/css2?family=Montserrat:wght@400;500;600;700&display=swap" rel="stylesheet">
<style>
:root{
  --navy:#0a3f73;
  --navy-deep:#063a6b;
  --ink:#0d3a68;
  --accent:#4a8fdc;
  --accent-soft:#dbe8f6;
  --card:#e1ebf7;
  --news-card:#f4f4f4;
  --text:#1c2f4a;
  --muted:#7c8796;
  --white:#ffffff;
}
*{box-sizing:border-box;margin:0;padding:0}
html,body{width:1200px;height:3348px;overflow:hidden}
body{position:relative;background:var(--white);font-family:'Montserrat',sans-serif;color:var(--text)}
.abs{position:absolute}
a{color:inherit;text-decoration:none}

/* hero */
.hero-panel{left:614px;top:0;width:586px;height:698px;background:var(--navy)}
.hero-photo{left:458px;top:60px;width:602px;height:638px;background:linear-gradient(180deg,#cdd8e6 0%,#8aa4c4 50%,#3a6596 100%)}
.menu-icon{right:18px;top:14px}
.brand{left:66px;top:50px;font-size:24px;font-weight:700;color:var(--ink);letter-spacing:.5px;display:flex;align-items:center;gap:10px}
.brand .dot{width:14px;height:14px;border-radius:50%;background:var(--accent)}
.client-login{left:474px;top:80px;font-size:11px;font-weight:500;color:var(--ink);display:flex;align-items:center;gap:6px}
.hero-title{left:66px;top:196px;width:560px;font-size:27px;font-weight:700;line-height:32px;color:var(--ink)}
.hero-title span,.sec-title span{color:var(--accent)}
.hero-lead{left:66px;top:270px;width:400px;font-size:17px;line-height:21px;color:var(--ink)}
.btn-outline{left:66px;top:362px;width:183px;height:37px;border:2px solid var(--accent);border-radius:20px;font-size:12px;font-weight:600;color:var(--accent);display:flex;align-items:center;justify-content:center}
.scroll-link{font-size:15px;color:var(--accent);display:flex;align-items:center;gap:6px}
.side-nav{left:1140px;top:505px;color:#8fb4e0;font-size:10px}
.side-nav .label{transform:rotate(90deg);transform-origin:left top;position:absolute;left:12px;top:0;white-space:nowrap}
.side-nav .rule{position:absolute;left:12px;top:70px;width:1px;height:48px;background:#8fb4e0}
.side-nav .nums{position:absolute;left:4px;top:125px;font-size:8px;font-weight:700;line-height:10px;color:#b8d0ee}
.side-nav .nums b{color:var(--white)}

/* sections */
.sec-line{height:3px;background:var(--accent)}
.sec-line::after{content:"";position:absolute;right:-6px;top:-5px;width:13px;height:13px;border-radius:50%;background:var(--accent)}
.sec-title{font-size:22px;font-weight:700;color:var(--ink)}
.body-copy{font-size:15px;line-height:18.5px;color:var(--ink)}

.about-backdrop{left:780px;top:700px;width:320px;height:560px;background:radial-gradient(ellipse at center,#e3edf8 0%,#eef4fb 55%,rgba(255,255,255,0) 75%)}
.about-photo{left:586px;top:833px;width:290px;height:290px;border-radius:50%;background:linear-gradient(160deg,#cfd2d8 0%,#7c828d 55%,#e6e7ea 100%)}
.about-ring{left:572px;top:819px;width:318px;height:318px;border-radius:50%;border:14px solid var(--accent-soft)}

/* positions */
.jobs{left:117px;top:1469px;display:grid;grid-template-columns:repeat(3,308px);column-gap:24px;row-gap:19px}
.job{height:86px;background:var(--card);border-left:5px solid var(--accent);padding:12px 22px;display:flex;flex-direction:column;justify-content:space-between}
.job h3{font-size:16px;font-weight:600;color:var(--ink);line-height:20px}
.job .loc{font-size:14px;color:#3b6fae;display:flex;align-items:center;gap:6px}

/* culture */
.culture-circle{left:877px;top:1943px;width:378px;height:378px;border-radius:50%;background:var(--accent-soft)}
.culture-video{left:663px;top:2006px;width:403px;height:269px;background:linear-gradient(180deg,#8fa6cc 0%,#6f7fa6 45%,#2b3550 55%,#5b6b8d 100%)}
.culture-video .play{position:absolute;left:182px;top:115px}
.icon-link{font-size:18px;color:var(--accent);display:flex;align-items:center;gap:10px}

/* news */
.news{top:2434px;width:269px;height:355px;background:var(--news-card)}
.news .thumb{height:176px}
.news .copy{padding:20px 15px 0}
.news h3{font-size:17px;font-weight:700;line-height:20px;color:var(--ink)}
.news p{margin-top:12px;font-size:13.5px;line-height:16.5px;color:#555e6b}
.news .more{position:absolute;right:10px;bottom:10px;font-size:13px;font-weight:600;color:var(--ink)}

/* offices */
.offices{left:0;top:2880px;width:1200px;height:217px;background:var(--navy-deep);color:var(--white)}
.office{position:absolute;top:52px}
.office h4{font-size:18px;font-weight:600}
.office ul{list-style:none;margin-top:14px;padding-left:15px;font-size:15px;line-height:19px}
.office li{display:flex;gap:8px;margin-bottom:8px}
.office li svg{flex:none;margin-top:2px}
.divider{position:absolute;top:45px;width:1px;height:110px;background:#ffffff88}

/* footer */
.foot-brand{left:72px;top:3140px;font-size:17px;font-weight:700;color:var(--ink);display:flex;align-items:center;gap:8px}
.foot-brand .dot{width:10px;height:10px;border-radius:50%;background:var(--accent)}
.foot-about{left:68px;top:3190px;width:325px;font-size:13px;line-height:16px;color:var(--accent)}
.foot-col{top:3165px}
.foot-col h5{font-size:18px;font-weight:600;color:var(--ink);margin-bottom:10px}
.foot-col a{display:block;font-size:14px;line-height:24px;color:var(--muted)}
.copyright{left:68px;top:3310px;font-size:11px;color:#9aa6b8}
</style>
</head>
<body>

<!-- hero -->
<div class="abs hero-panel"></div>
<div class="abs hero-photo" role="img" aria-label="Photograph of tall glass skyscrapers against a blue sky"></div>
<svg class="abs menu-icon" width="40" height="40" viewBox="0 0 40 40"><path d="M14 8 L6 16 M22 8 L6 24 M30 8 L6 32" stroke="#fff" stroke-width="3" fill="none"/></svg>

<div class="abs brand"><span class="dot"></span>Harlow Vectors</div>
<a class="abs client-login" href="#"><svg width="12" height="12" viewBox="0 0 12 12"><circle cx="6" cy="3.5" r="3" fill="#0d3a68"/><path d="M0 12a6 5 0 0 1 12 0z" fill="#0d3a68"/></svg>Already a Client?</a>

<h1 class="abs hero-title">Bringing AI and Statistical Inference<br>to <span>Financial Markets</span></h1>
<p class="abs hero-lead">Harlow Vectors is a quantitative asset manager with the singular focus of delivering algorithmic strategies that work</p>
<a class="abs btn-outline" href="#">GET IN TOUCHE</a>
<a class="abs scroll-link" href="#" style="left:70px;top:603px"><svg width="14" height="16" viewBox="0 0 14 16"><path d="M7 1v13M1 8l6 6 6-6" stroke="#4a8fdc" stroke-width="1.6" fill="none"/></svg>What We Do?</a>

<div class="abs side-nav">
  <span class="label">Our Value</span>
  <span class="rule"></span>
  <div class="nums"><b>01</b><br>02<br>03</div>
</div>

<!-- what we do -->
<div class="abs about-backdrop" role="img" aria-label="Faint decorative connected-nodes motif"></div>
<div class="abs sec-line" style="left:0;top:834px;width:202px"></div>
<h2 class="abs sec-title" style="left:225px;top:821px">What <span>We Do</span>?</h2>
<p class="abs body-copy" style="left:200px;top:862px;width:318px">We deliver consistent alpha across liquid markets through the application of proprietary IP in Bayesian inference, machine learning and artificial intelligence. We are a multi-disciplinary team founded by experienced finance professionals from premier institutions, leading academics from the Thornbury Stellar Unit at Ashmere College and world-class software engineers.</p>
<div class="abs about-ring"></div>
<div class="abs about-photo" role="img" aria-label="Desk with a laptop, phone and ring binder during a working meeting"></div>
<a class="abs scroll-link" href="#" style="left:205px;top:1183px"><svg width="14" height="16" viewBox="0 0 14 16"><path d="M7 1v13M1 8l6 6 6-6" stroke="#4a8fdc" stroke-width="1.6" fill="none"/></svg>Our Open Positions</a>

<!-- positions -->
<div class="abs sec-line" style="left:0;top:1361px;width:116px"></div>
<h2 class="abs sec-title" style="left:139px;top:1349px">Our <span>Open</span> Positions</h2>
<p class="abs body-copy" style="left:117px;top:1392px;width:950px">We are always looking for exceptional talent to join our entrepreneurial team. We are looking for individuals who are creative thinkers, can demonstrate analytical rigour and are passionate about the intersection of science, finance and technology</p>

<div class="abs jobs">
  <div class="job"><h3>Growth Marketer</h3><span class="loc"><svg width="10" height="13" viewBox="0 0 10 13"><path d="M5 0a5 5 0 0 1 5 5c0 3-5 8-5 8S0 8 0 5a5 5 0 0 1 5-5z" fill="#0d3a68"/><circle cx="5" cy="5" r="1.8" fill="#e1ebf7"/></svg>Cambridge</span></div>
  <div class="job"><h3>Graphic Designer</h3><span class="loc"><svg width="10" height="13" viewBox="0 0 10 13"><path d="M5 0a5 5 0 0 1 5 5c0 3-5 8-5 8S0 8 0 5a5 5 0 0 1 5-5z" fill="#0d3a68"/><circle cx="5" cy="5" r="1.8" fill="#e1ebf7"/></svg>London</span></div>
  <div class="job"><h3>Market Strategist</h3><span class="loc"><svg width="10" height="13" viewBox="0 0 10 13"><path d="M5 0a5 5 0 0 1 5 5c0 3-5 8-5 8S0 8 0 5a5 5 0 0 1 5-5z" fill="#0d3a68"/><circle cx="5" cy="5" r="1.8" fill="#e1ebf7"/></svg>Cambridge</span></div>
  <div class="job"><h3>Software Engineer (Computer Science)</h3><span class="loc"><svg width="10" height="13" viewBox="0 0 10 13"><path d="M5 0a5 5 0 0 1 5 5c0 3-5 8-5 8S0 8 0 5a5 5 0 0 1 5-5z" fill="#0d3a68"/><circle cx="5" cy="5" r="1.8" fill="#e1ebf7"/></svg>London</span></div>
  <div class="job"><h3>Growth Marketer</h3><span class="loc"><svg width="10" height="13" viewBox="0 0 10 13"><path d="M5 0a5 5 0 0 1 5 5c0 3-5 8-5 8S0 8 0 5a5 5 0 0 1 5-5z" fill="#0d3a68"/><circle cx="5" cy="5" r="1.8" fill="#e1ebf7"/></svg>Singapore</span></div>
  <div class="job"><h3>Growth Marketer</h3><span class="loc"><svg width="10" height="13" viewBox="0 0 10 13"><path d="M5 0a5 5 0 0 1 5 5c0 3-5 8-5 8S0 8 0 5a5 5 0 0 1 5-5z" fill="#0d3a68"/><circle cx="5" cy="5" r="1.8" fill="#e1ebf7"/></svg>Cambridge</span></div>
  <div class="job"><h3>Growth Marketer</h3><span class="loc"><svg width="10" height="13" viewBox="0 0 10 13"><path d="M5 0a5 5 0 0 1 5 5c0 3-5 8-5 8S0 8 0 5a5 5 0 0 1 5-5z" fill="#0d3a68"/><circle cx="5" cy="5" r="1.8" fill="#e1ebf7"/></svg>Singapore</span></div>
  <div class="job"><h3>Graphic Designer</h3><span class="loc"><svg width="10" height="13" viewBox="0 0 10 13"><path d="M5 0a5 5 0 0 1 5 5c0 3-5 8-5 8S0 8 0 5a5 5 0 0 1 5-5z" fill="#0d3a68"/><circle cx="5" cy="5" r="1.8" fill="#e1ebf7"/></svg>London</span></div>
  <div class="job"><h3>Market Strategist</h3><span class="loc"><svg width="10" height="13" viewBox="0 0 10 13"><path d="M5 0a5 5 0 0 1 5 5c0 3-5 8-5 8S0 8 0 5a5 5 0 0 1 5-5z" fill="#0d3a68"/><circle cx="5" cy="5" r="1.8" fill="#e1ebf7"/></svg>London</span></div>
  <div class="job"><h3>Software Engineer (Computer Science)</h3><span class="loc"><svg width="10" height="13" viewBox="0 0 10 13"><path d="M5 0a5 5 0 0 1 5 5c0 3-5 8-5 8S0 8 0 5a5 5 0 0 1 5-5z" fill="#0d3a68"/><circle cx="5" cy="5" r="1.8" fill="#e1ebf7"/></svg>Singapore</span></div>
  <div class="job"><h3>Growth Marketer</h3><span class="loc"><svg width="10" height="13" viewBox="0 0 10 13"><path d="M5 0a5 5 0 0 1 5 5c0 3-5 8-5 8S0 8 0 5a5 5 0 0 1 5-5z" fill="#0d3a68"/><circle cx="5" cy="5" r="1.8" fill="#e1ebf7"/></svg>Singapore</span></div>
</div>

<!-- culture -->
<div class="abs culture-circle"></div>
<div class="abs sec-line" style="left:0;top:2017px;width:150px"></div>
<h2 class="abs sec-title" style="left:173px;top:2005px">Our <span>Culture</span></h2>
<p class="abs body-copy" style="left:140px;top:2052px;width:450px">We prioritise having a company culture that promotes sharing ideas in a safe, collaborative research environment. We make sure that every member of the team has the opportunity to explore their own ideas through weekly 'innovation time', and ensure that everyone gets the support they need to continue to grow as individuals within the company.</p>
<a class="abs icon-link" href="#" style="left:140px;top:2198px"><svg width="24" height="24" viewBox="0 0 24 24"><circle cx="12" cy="12" r="11" stroke="#4a8fdc" stroke-width="2" fill="none"/><path d="M9.5 7.5v9l7-4.5z" fill="#4a8fdc"/></svg>Get To Know Us</a>
<div class="abs culture-video" role="img" aria-label="City skyline at dusk reflected in calm water, video thumbnail">
  <svg class="play" width="40" height="40" viewBox="0 0 40 40"><circle cx="20" cy="20" r="18" stroke="#fff" stroke-width="2.5" fill="none"/><path d="M16 12v16l12-8z" fill="#fff"/></svg>
</div>

<!-- news -->
<div class="abs sec-line" style="left:0;top:2375px;width:148px"></div>
<h2 class="abs sec-title" style="left:170px;top:2363px">Our Latest <span>News</span></h2>

<article class="abs news" style="left:150px">
  <div class="thumb" role="img" aria-label="Robotic hand reaching toward a human hand on a pale blue background" style="background:linear-gradient(135deg,#b9cdea,#7fa0d6)"></div>
  <div class="copy"><h3>How is AI changing the financial World</h3><p>Lorem Ipsum is simply dummy text of the printing and typesetting industry. Lorem Ipsum has been the industry's...</p></div>
  <a class="more" href="#">Continue reading &gt;&gt;</a>
</article>
<article class="abs news" style="left:459px">
  <div class="thumb" role="img" aria-label="Person wearing a glowing virtual reality headset" style="background:linear-gradient(160deg,#0d1a3a,#274a86 60%,#6b82b3)"></div>
  <div class="copy"><h3>VR applications in the current market</h3><p>Lorem Ipsum is simply dummy text of the printing and typesetting industry. Lorem Ipsum has been the industry's...</p></div>
  <a class="more" href="#">Continue reading &gt;&gt;</a>
</article>
<article class="abs news" style="left:768px">
  <div class="thumb" role="img" aria-label="White toy robot on a purple-blue background" style="background:linear-gradient(135deg,#3b47a8,#7b8fd6 60%,#cfd6ef)"></div>
  <div class="copy"><h3>How is AI changing the financial World</h3><p>Lorem Ipsum is simply dummy text of the printing and typesetting industry. Lorem Ipsum has been the industry's...</p></div>
  <a class="more" href="#">Continue reading &gt;&gt;</a>
</article>

<!-- offices -->
<section class="abs offices">
  <div class="office" style="left:68px">
    <h4>Cambridge Office</h4>
    <ul>
      <li><svg width="14" height="14" viewBox="0 0 14 14"><path d="M1 14V3h8v11zM9 14V7h4v7z" fill="#fff"/></svg><span>3441 Walnut Avenue<br>Brindle Hollow,</span></li>
      <li><svg width="14" height="11" viewBox="0 0 14 11"><rect width="14" height="11" rx="1" fill="#fff"/><path d="M1 1l6 5 6-5" stroke="#063a6b" stroke-width="1.3" fill="none"/></svg>contact@harlowvectors.example</li>
      <li><svg width="14" height="14" viewBox="0 0 14 14"><path d="M3 0l3 3-1.5 2a8 8 0 0 0 4.5 4.5L11 8l3 3-2 2.5C6 13 1 8 .5 2z" fill="#fff"/></svg>+00 123-456-89</li>
    </ul>
  </div>
  <div class="divider" style="left:416px"></div>
  <div class="office" style="left:450px">
    <h4>London Office</h4>
    <ul>
      <li><svg width="14" height="14" viewBox="0 0 14 14"><path d="M1 14V3h8v11zM9 14V7h4v7z" fill="#fff"/></svg><span>3441 Walnut Avenue<br>Brindle Hollow,</span></li>
      <li><svg width="14" height="11" viewBox="0 0 14 11"><rect width="14" height="11" rx="1" fill="#fff"/><path d="M1 1l6 5 6-5" stroke="#063a6b" stroke-width="1.3" fill="none"/></svg>contact@harlowvectors.example</li>
      <li><svg width="14" height="14" viewBox="0 0 14 14"><path d="M3 0l3 3-1.5 2a8 8 0 0 0 4.5 4.5L11 8l3 3-2 2.5C6 13 1 8 .5 2z" fill="#fff"/></svg>+00 123-456-89</li>
    </ul>
  </div>
  <div class="divider" style="left:784px"></div>
  <div class="office" style="left:824px">
    <h4>Singapore Office</h4>
    <ul>
      <li><svg width="14" height="14" viewBox="0 0 14 14"><path d="M1 14V3h8v11zM9 14V7h4v7z" fill="#fff"/></svg><span>3441 Walnut Avenue<br>Brindle Hollow,</span></li>
      <li><svg width="14" height="11" viewBox="0 0 14 11"><rect width="14" height="11" rx="1" fill="#fff"/><path d="M1 1l6 5 6-5" stroke="#063a6b" stroke-width="1.3" fill="none"/></svg>contact@harlowvectors.example</li>
      <li><svg width="14" height="14" viewBox="0 0 14 14"><path d="M3 0l3 3-1.5 2a8 8 0 0 0 4.5 4.5L11 8l3 3-2 2.5C6 13 1 8 .5 2z" fill="#fff"/></svg>+00 123-456-89</li>
    </ul>
  </div>
</section>

<!-- footer -->
<div class="abs foot-brand"><span class="dot"></span>Harlow Vectors</div>
<p class="abs foot-about">Lorem Ipsum is simply dummy text of the printing and typesetting industry. Lorem Ipsum has been the industry's standard dummy text ever since the 1500s, when an unknown printer took a galley of type and scrambled it to make a type specimen book.</p>
<nav class="abs foot-col" style="left:508px"><h5>Usefull Links</h5><a href="#">Clients Space</a><a href="#">Latest News</a><a href="#">Privacy Policy</a></nav>
<nav class="abs foot-col" style="left:738px"><h5>Site Map</h5><a href="#">Our Culture</a><a href="#">Our Open Job Positions</a><a href="#">What does Our Logo Mean</a><a href="#">Our Values</a></nav>
<nav class="abs foot-col" style="left:1008px"><h5>Usefull Links</h5><a href="#">Clients Space</a><a href="#">Latest News</a><a href="#">Privacy Policy</a></nav>
<p class="abs copyright">2021 © HARLOW VECTORS | ALL RIGHTS RESERVED</p>

</body>
</html>
```